KVT Business Cards

We require business cards for our business. We would like a matte black back to the card, with our logo centred in the middle. The front side of the card is open to design.

Target Market(s)

Clients looking for legal services (professional)

Industry/Entity Type

Legal

Contact Information for Business Card

Boris Telemark
Partner
Mobile: 0438 715 642
Email: boris@kvtlaw.co
Website: www.kvtlaw.co
Level 3, 118 Wexbury Street
Sydney NSW 2000

Font styles to use
Other font styles liked:
• Avenir

Colors
f04a50
ffffff
1b1b1b

Requirements
Must have
• Black back with logo included in the centre of the card.
• Our font is Avenir.

```html
<!DOCTYPE html>
<html lang="en">
<head>
<meta charset="utf-8">
<title>KVT Business Cards</title>
<link href="https://fonts.googleapis.com/css2?family=Lato:wght@400;700;900&display=swap" rel="stylesheet">
<style>
  :root {
    --stage: #121212;
    --card: #1b1b1b;
    --accent: #c8244a;
    --white: #ffffff;
    --muted: #d9d9d9;
    --rule: #2c2c2c;
  }
  * { box-sizing: border-box; margin: 0; padding: 0; }
  html, body { width: 1200px; height: 900px; overflow: hidden; }
  body {
    background: var(--stage);
    font-family: "Lato", "Avenir", sans-serif;
    position: relative;
  }
  .card {
    position: absolute;
    width: 560px;
    height: 320px;
    background: var(--card);
    border-radius: 22px;
    box-shadow: 0 18px 40px rgba(0,0,0,.6);
    color: var(--white);
  }
  .card-back { left: 110px; top: 80px; }
  .card-front { left: 530px; top: 480px; }

  /* back */
  .back-mark {
    position: absolute; left: 0; right: 0; top: 100px;
    display: flex; justify-content: center; align-items: center; gap: 14px;
  }
  .mark-name {
    font-weight: 900; font-size: 64px; letter-spacing: 4px; line-height: 1;
  }
  .mark-square { width: 18px; height: 18px; }
  .back-mark .mark-name { color: var(--white); }
  .back-mark .mark-square { background: var(--white); }
  .back-web {
    position: absolute; right: 40px; bottom: 34px;
    font-size: 15px; color: var(--muted); letter-spacing: .5px;
  }

  /* front */
  .front-brand {
    position: absolute; left: 150px; top: 46px;
    display: flex; align-items: center; gap: 26px;
  }
  .front-brand .mark-name { color: var(--accent); font-size: 58px; }
  .front-brand .mark-square { background: var(--accent); }
  .firm-name {
    font-weight: 900; font-size: 22px; line-height: 1.05;
    letter-spacing: .5px; text-transform: uppercase; color: var(--white);
  }
  .front-rule {
    position: absolute; left: 30px; right: 30px; top: 160px;
    height: 1px; background: var(--rule);
  }
  .person { position: absolute; left: 40px; top: 182px; }
  .person-name {
    font-weight: 900; font-size: 18px; color: var(--accent);
    text-transform: uppercase; letter-spacing: .5px;
  }
  .person-role { font-size: 15px; color: var(--muted); margin-bottom: 8px; }
  .contact-list { list-style: none; }
  .contact-list li {
    display: flex; align-items: center; gap: 10px;
    font-size: 15px; color: var(--muted); line-height: 22px;
  }
  .contact-list svg { width: 12px; height: 12px; fill: var(--accent); }
  .address {
    position: absolute; right: 40px; top: 190px;
    font-size: 15px; line-height: 22px; color: var(--muted); text-align: left;
  }
</style>
</head>
<body>

<section class="card card-back" aria-label="Card back">
  <div class="back-mark">
    <span class="mark-name">KVT</span>
    <span class="mark-square"></span>
  </div>
  <p class="back-web">www.kvtlaw.co</p>
</section>

<section class="card card-front" aria-label="Card front">
  <div class="front-brand">
    <span class="mark-name">KVT</span>
    <p class="firm-name">Kestrel<br>Vance<br>Telemark</p>
  </div>
  <div class="front-rule"></div>

  <div class="person">
    <p class="person-name">Boris Telemark</p>
    <p class="person-role">Partner</p>
    <ul class="contact-list">
      <li>
        <svg viewBox="0 0 12 12" aria-hidden="true"><path d="M1 3c0-1 1-2 2-2l1.5 2.5L3.5 5c.7 1.5 2 2.8 3.5 3.5l1.5-1L11 9c0 1-1 2-2 2C4.6 11 1 7.4 1 3z"/></svg>
        0438 715 642
      </li>
      <li>
        <svg viewBox="0 0 12 12" aria-hidden="true"><path d="M0 2h12v8H0z M1 3l5 4 5-4" stroke="#1b1b1b" stroke-width="1"/></svg>
        boris@kvtlaw.co
      </li>
      <li>
        <svg viewBox="0 0 12 12" aria-hidden="true"><circle cx="6" cy="6" r="6"/><path d="M0 6h12M6 0c-3 3-3 9 0 12M6 0c3 3 3 9 0 12" stroke="#1b1b1b" stroke-width=".8" fill="none"/></svg>
        www.kvtlaw.co
      </li>
    </ul>
  </div>

  <p class="address">Level 3, 118 Wexbury<br>Street, Sydney NSW 2000</p>
</section>

</body>
</html>
```